Business Card Design

We are a new company that grows and processes olives. We will be producing both olive oil and table olives. We will add grapes and wine making in about five years and hope to start a small restaurant with an observation window overlooking our olive processing area.
The design we have in mind is one that could be adapted to bottle lables for our olive products. Our thoughts are an oval design showing a night time view of a bay with a family of wolves resting on the shore. We would like a border on top of olive branches with olives. We are pretty open on the rest.

Industry/Entity Type

Restaurant

Contact Information for Business Card

Heron Creek Groves
18537 CR 41
Marlow Point, AL 36584
Dale Finch and Sabine Kowalczyk

```html
<!DOCTYPE html>
<html lang="en">
<head>
<meta charset="utf-8">
<title>Heron Creek Groves – Business Card</title>
<link rel="stylesheet" href="https://fonts.googleapis.com/css2?family=Ubuntu:wght@300;500&display=swap">
<style>
  :root {
    --page-bg: #ecebe6;
    --card-white: #ffffff;
    --lime: #b3cf1c;
    --olive: #8b9a24;
    --name-green: #7a8c1e;
    --text-light: #f4f6e6;
  }
  * { margin: 0; padding: 0; box-sizing: border-box; }
  html, body {
    width: 1200px;
    height: 809px;
    overflow: hidden;
    background: var(--page-bg);
  }
  .canvas {
    position: relative;
    width: 1200px;
    height: 809px;
  }
  .business-card {
    position: absolute;
    left: 150px;
    top: 147px;
    width: 900px;
    height: 514px;
    background: var(--card-white);
    overflow: hidden;
    box-shadow: 0 10px 30px rgba(0,0,0,0.12);
    font-family: "Ubuntu", sans-serif;
  }
  .top-stripe {
    position: absolute;
    left: 0; top: 0;
    width: 100%;
    height: 12px;
    background: var(--lime);
  }
  .logo-block {
    position: absolute;
    left: 0;
    top: 80px;
    width: 100%;
    height: 160px;
    display: flex;
    align-items: center;
    justify-content: center;
    gap: 22px;
  }
  .company-name {
    font-weight: 500;
    font-size: 56px;
    line-height: 1;
    color: var(--name-green);
    white-space: nowrap;
  }
  .logo-mark {
    flex: none;
    width: 44px;
    height: 44px;
    border-radius: 50%;
    background: var(--name-green);
  }
  .contact-band {
    position: absolute;
    left: 0;
    top: 296px;
    width: 100%;
    height: 218px;
    background: var(--olive);
    border-top: 7px solid var(--lime);
  }
  .contact-details {
    position: absolute;
    left: 180px;
    top: 36px;
    color: var(--text-light);
    font-style: normal;
    font-weight: 300;
    font-size: 30px;
    line-height: 1.35;
    white-space: nowrap;
  }
</style>
</head>
<body>
  <main class="canvas">
    <article class="business-card">
      <div class="top-stripe"></div>
      <header class="logo-block">
        <h1 class="company-name">Heron Creek Groves</h1>
        <span class="logo-mark" aria-hidden="true"></span>
      </header>
      <section class="contact-band">
        <address class="contact-details">
          <div class="street-address">18537 CR 41 Marlow Point, AL 36584</div>
          <div class="owners">Dale Finch and Sabine Kowalczyk</div>
        </address>
      </section>
    </article>
  </main>
</body>
</html>
```